Project Report for American Indian and Alaska Native org (U.S.)

We need a report formatted/ design / layout.
We are a nonprofit organization that works on indigenous elder issues.
The report should reflect our logo color scheme.
Body font should be at least 11 point sans serif.
Ideally, headings and title would use fonts that are reminiscent of tribal cultures though not hard to read or whimsical/ unprofessional looking.

We have used some light script style fonts in the past -- nothing too cursive looking though.

The audience is public health professionals and tribal staff and leadership.

We want our organization's logo (QR7) and the project logo (brain health) incorporated into the title page.

We prefer the files to come back to us in an editable fashion + a pdf file.

Industry/Entity Type

tribal communities and public health officials

Font styles to use
Serif
Sans Serif

Requirements
Must have
• our logo and color scheme
Should not have
• headdress images

```html
<!DOCTYPE html>
<html lang="en">
<head>
<meta charset="utf-8">
<title>Tribal Law &amp; Policy Report Layout</title>
<link rel="stylesheet" href="https://fonts.googleapis.com/css2?family=Montserrat:wght@400;600;700;800&family=Open+Sans:wght@400;600;700&display=swap">
<style>
:root{
  --bg:#e4e7e9;
  --paper:#ffffff;
  --teal:#3b9ea6;
  --teal-dark:#2a7c84;
  --teal-light:#d9eef0;
  --rust:#b9533f;
  --rust-light:#e9a48f;
  --ink:#3c4146;
  --muted:#8a9096;
  --photo-a:#b9c4b0;
  --photo-b:#d8c6b4;
  --photo-c:#a7b8bf;
}
*{box-sizing:border-box;margin:0;padding:0}
html,body{width:1200px;height:2776px;overflow:hidden}
body{background:var(--bg);font-family:"Open Sans",Arial,sans-serif;color:var(--ink);position:relative}
.page{position:absolute;background:var(--paper);box-shadow:0 3px 10px rgba(0,0,0,.14);overflow:hidden;padding:34px 32px}
.page::before{content:"";position:absolute;inset:12px;border-top:1.5px solid var(--teal);border-left:1.5px solid var(--teal);border-right:1.5px solid var(--rust);border-bottom:1.5px solid var(--rust);pointer-events:none}
.cover{left:430px;top:180px;width:340px;height:470px}
.p-contents{left:160px;top:800px;width:400px;height:518px}
.p-summary{left:640px;top:800px;width:400px;height:518px}
.p-background{left:160px;top:1420px;width:400px;height:518px}
.p-strategies{left:640px;top:1420px;width:400px;height:518px}
.p-actions{left:160px;top:2040px;width:400px;height:518px}
.p-sovereignty{left:640px;top:2040px;width:400px;height:518px}

.brand{display:flex;align-items:center;gap:5px;font-family:"Montserrat",sans-serif;font-weight:800;color:var(--teal-dark);font-size:13px;letter-spacing:.5px}
.brand-dot{width:10px;height:10px;border-radius:50%;background:var(--rust)}
.page-header{display:flex;justify-content:flex-end}
.page-footer{position:absolute;left:32px;right:32px;bottom:24px;display:flex;justify-content:space-between;align-items:center}
.page-footer .brand{font-size:10px}
.page-footer .brand-dot{width:7px;height:7px}
.page-num{background:var(--rust);color:#fff;font-family:"Montserrat",sans-serif;font-weight:700;font-size:7px;padding:2px 8px;border-radius:8px}

.photo{border-radius:2px}
.photo-a{background:linear-gradient(135deg,var(--photo-a),var(--photo-b))}
.photo-b{background:linear-gradient(135deg,var(--photo-b),#c89e86)}
.photo-c{background:linear-gradient(135deg,var(--photo-c),var(--photo-a))}

p.body{font-size:5.2px;line-height:7.4px;margin-bottom:5px;text-align:justify}
.band{display:inline-block;font-family:"Montserrat",sans-serif;font-weight:800;color:#fff;letter-spacing:.6px;padding:4px 10px;font-size:11px}
.band-teal{background:var(--teal)}
.band-rust{background:var(--rust)}

/* cover */
.cover .page-header{margin-bottom:14px}
.cover-title{text-align:center;font-family:"Montserrat",sans-serif}
.cover-kicker{color:var(--teal-dark);font-weight:800;font-size:12px;letter-spacing:.6px}
.cover-line{display:inline-block;color:#fff;font-weight:800;font-size:15px;padding:3px 10px;margin:3px 0;letter-spacing:.4px}
.cover-and{color:var(--rust);font-weight:700;font-size:8px;letter-spacing:1px}
.cover-photo{height:150px;margin:10px 0 12px}
.cover-meta{text-align:center;font-family:"Montserrat",sans-serif}
.cover-meta .prepared{display:inline-block;background:var(--teal);color:#fff;font-size:6px;font-weight:700;padding:2px 8px;letter-spacing:.8px}
.cover-meta .date{color:var(--rust);font-weight:800;font-size:17px;letter-spacing:1px;margin-top:3px}

/* contents */
.contents-box{margin-top:26px;border:1px solid #dcdfe2;background:#f6f7f8;padding:16px 20px}
.contents-title{font-family:"Montserrat",sans-serif;font-weight:800;color:#fff;background:var(--rust);display:inline-block;font-size:11px;padding:3px 12px;margin:-26px 0 12px -20px}
.toc li{list-style:none;display:flex;font-size:6px;line-height:14.5px;font-weight:600}
.toc li .lead{flex:1;border-bottom:1px dotted var(--muted);margin:0 4px 4px}
.toc li .n{color:var(--rust);font-weight:700}

/* summary */
.doc-title{font-family:"Montserrat",sans-serif;font-weight:700;color:var(--ink);font-size:12px;line-height:15px;margin:14px 0 10px}
.doc-title span{font-weight:400}
.summary-grid{display:grid;grid-template-columns:1fr 130px;gap:12px;margin-top:10px}
.summary-photo{height:150px;border-bottom:4px solid var(--rust)}

/* background */
.bg-box{display:grid;grid-template-columns:110px 1fr;gap:10px;background:var(--teal-light);padding:10px;margin:6px 0 8px}
.bg-box h4{font-family:"Montserrat",sans-serif;font-size:7px;color:var(--teal-dark);font-weight:800;line-height:9px;margin-bottom:4px}
.donut-wrap{display:flex;align-items:center;gap:6px}
.donut-labels{font-size:4.6px;line-height:6px;font-weight:600}
.donut-labels .t{color:var(--teal-dark)}
.donut-labels .r{color:var(--rust)}
.photo-row{display:grid;grid-template-columns:1fr 1fr;gap:8px}

/* strategies */
.strat-top{display:grid;grid-template-columns:140px 1fr;gap:10px}

/* actions */
.actions-box{background:var(--teal-light);padding:12px 14px;margin-top:8px}
.actions-box h3{font-family:"Montserrat",sans-serif;font-size:8px;font-weight:800;color:var(--teal-dark);margin-bottom:8px;display:flex;align-items:center;gap:5px}
.action-grid{display:grid;grid-template-columns:1fr 1fr;gap:8px 12px}
.action{display:grid;grid-template-columns:20px 1fr;gap:5px;align-items:start}
.action .ico{width:20px;height:20px;border-radius:50%;background:var(--teal);display:flex;align-items:center;justify-content:center}
.action .ico.alt{background:var(--rust)}
.action b{display:block;font-family:"Montserrat",sans-serif;font-size:5.4px;color:var(--ink);font-weight:800;margin-bottom:1px}
.action span{font-size:4.6px;line-height:6px;display:block}
</style>
</head>
<body>

<!-- Cover -->
<section class="page cover">
  <div class="page-header"><div class="brand"><span class="brand-dot"></span>QR7</div></div>
  <div class="cover-title">
    <div class="cover-kicker">TRIBAL LAW &amp; POLICY:</div>
    <div class="cover-line band-rust">ALZHEIMER'S DISEASE</div><br>
    <div class="cover-and">AND RELATED</div>
    <div class="cover-line band-teal">DEMENTIA ISSUES</div>
  </div>
  <div class="cover-photo photo photo-a" role="img" aria-label="Photograph of smiling elder couple outdoors"></div>
  <div class="cover-meta">
    <div class="prepared">PREPARED BY PROJECT STAFF</div>
    <div class="date">OCTOBER 27 | 2021</div>
  </div>
</section>

<!-- Contents -->
<section class="page p-contents">
  <div class="page-header"><div class="brand"><span class="brand-dot"></span>QR7</div></div>
  <div class="contents-box">
    <div class="contents-title">CONTENTS</div>
    <ul class="toc">
      <li>Executive Summary<span class="lead"></span><span class="n">03</span></li>
      <li>Background<span class="lead"></span><span class="n">04</span></li>
      <li>Tribal Sovereignty<span class="lead"></span><span class="n">06</span></li>
      <li>Role of Public Health<span class="lead"></span><span class="n">07</span></li>
      <li>Methods<span class="lead"></span><span class="n">08</span></li>
      <li>Findings<span class="lead"></span><span class="n">09</span></li>
      <li>Guardianship and Conservatorship<span class="lead"></span><span class="n">10</span></li>
      <li>Elder Protection Codes<span class="lead"></span><span class="n">11</span></li>
      <li>Adult Protective Services<span class="lead"></span><span class="n">12</span></li>
      <li>Caregiver Support<span class="lead"></span><span class="n">13</span></li>
      <li>Long-Term Care Laws<span class="lead"></span><span class="n">14</span></li>
      <li>Public Health Infrastructure<span class="lead"></span><span class="n">15</span></li>
      <li>State and Tribal Agreements<span class="lead"></span><span class="n">16</span></li>
      <li>Recommendations<span class="lead"></span><span class="n">17</span></li>
      <li>Conclusion<span class="lead"></span><span class="n">18</span></li>
      <li>References<span class="lead"></span><span class="n">19</span></li>
    </ul>
  </div>
  <div class="page-footer"><div class="brand"><span class="brand-dot"></span>QR7</div><span class="page-num">02</span></div>
</section>

<!-- Executive summary -->
<section class="page p-summary">
  <h1 class="doc-title">Tribal Law and Policy Regarding<br><span>Alzheimer's Disease and Related Dementia Issues</span></h1>
  <div class="band band-teal">EXECUTIVE SUMMARY</div>
  <div class="summary-grid">
    <div>
      <p class="body">Tribal nations hold the inherent authority to protect the health and wellbeing of their citizens, including elders living with Alzheimer's disease and related dementias. This report reviews how tribal codes, policies and agreements address memory loss, caregiving and elder protection across Indian Country.</p>
      <p class="body">Our review found that many communities rely on general elder protection laws that do not name dementia directly. Few codes address capacity, decision making or the needs of family caregivers who provide most daily care at home.</p>
      <p class="body">We offer practical options that tribal leaders and public health staff can adapt to their own traditions, values and governing structures, along with examples drawn from existing codes.</p>
      <p class="body">The findings are meant to support planning, open conversations and strengthen the systems that keep elders safe, respected and connected to community.</p>
    </div>
    <div class="summary-photo photo photo-b" role="img" aria-label="Photograph of an elder woman seated by a window"></div>
  </div>
  <div class="page-footer"><div class="brand"><span class="brand-dot"></span>QR7</div><span class="page-num">03</span></div>
</section>

<!-- Background -->
<section class="page p-background">
  <div class="band band-teal">BACKGROUND</div>
  <p class="body" style="margin-top:8px">Alzheimer's disease and related dementias affect a growing number of American Indian and Alaska Native elders. Rates of risk factors such as diabetes, hypertension and heart disease are higher in many tribal communities, and access to diagnosis and specialty care is often limited by distance and funding.</p>
  <div class="bg-box">
    <div>
      <h4>THE ALZHEIMER'S PUBLIC HEALTH ROAD MAP</h4>
      <p class="body">The road map outlines actions public health agencies can take to promote brain health, detect memory loss early and support caregivers across the life course.</p>
    </div>
    <div class="donut-wrap">
      <svg width="96" height="96" viewBox="0 0 96 96" role="img" aria-label="Donut chart of four action domains">
        <circle cx="48" cy="48" r="32" fill="none" stroke="#3b9ea6" stroke-width="22" stroke-dasharray="50 151" transform="rotate(-90 48 48)"/>
        <circle cx="48" cy="48" r="32" fill="none" stroke="#b9533f" stroke-width="22" stroke-dasharray="50 151" stroke-dashoffset="-50.3" transform="rotate(-90 48 48)"/>
        <circle cx="48" cy="48" r="32" fill="none" stroke="#2a7c84" stroke-width="22" stroke-dasharray="50 151" stroke-dashoffset="-100.6" transform="rotate(-90 48 48)"/>
        <circle cx="48" cy="48" r="32" fill="none" stroke="#e9a48f" stroke-width="22" stroke-dasharray="50 151" stroke-dashoffset="-150.9" transform="rotate(-90 48 48)"/>
        <circle cx="48" cy="48" r="20" fill="#fff"/>
      </svg>
      <div class="donut-labels">
        <div class="t">Educate &amp; Empower</div>
        <div class="r">Develop Policies</div>
        <div class="t">Assure Workforce</div>
        <div class="r">Monitor &amp; Evaluate</div>
      </div>
    </div>
  </div>
  <p class="body">Tribal public health programs are well placed to lead this work by pairing cultural knowledge with data, partnerships and policy tools that reflect community priorities.</p>
  <div class="photo-row">
    <div class="photo photo-c" style="height:70px" role="img" aria-label="Photograph of a caregiver with an elder"></div>
    <div class="photo photo-a" style="height:70px" role="img" aria-label="Photograph of hands held together"></div>
  </div>
  <div class="page-footer"><div class="brand"><span class="brand-dot"></span>QR7</div><span class="page-num">04</span></div>
</section>

<!-- Strategies -->
<section class="page p-strategies">
  <div class="strat-top">
    <div class="photo photo-b" style="height:120px" role="img" aria-label="Photograph of an elder man resting"></div>
    <div>
      <p class="body">Families are the first line of care for elders with memory loss. Many caregivers balance work, children and cultural responsibilities while providing support with little outside help or training.</p>
      <p class="body">Community health representatives, elder programs and clinics each see part of the picture. Coordinated policy can connect these efforts so elders receive timely screening and services close to home.</p>
    </div>
  </div>
  <div class="band band-rust" style="margin:10px 0 8px">STRATEGIES FOR TRIBAL NATIONS</div>
  <p class="body">Tribes can adopt codes that define vulnerable adults, set reporting duties and create protective orders suited to dementia. Policies may also recognize traditional decision making within families and clans.</p>
  <p class="body">Agreements with states and counties can clarify jurisdiction, share data and ensure that elders are not left without protection when they move between service systems.</p>
  <div class="photo-row" style="margin-top:6px">
    <div class="photo photo-a" style="height:78px" role="img" aria-label="Photograph of elders walking outdoors"></div>
    <div class="photo photo-c" style="height:78px" role="img" aria-label="Photograph of an elder exercising with a helper"></div>
  </div>
  <div class="page-footer"><div class="brand"><span class="brand-dot"></span>QR7</div><span class="page-num">05</span></div>
</section>

<!-- Actions -->
<section class="page p-actions">
  <div class="actions-box">
    <h3><svg width="10" height="10" viewBox="0 0 10 10"><circle cx="5" cy="5" r="5" fill="#b9533f"/><path d="M2.8 5.2l1.5 1.5 3-3" stroke="#fff" stroke-width="1.2" fill="none"/></svg>PUBLIC HEALTH ACTIONS FOR BRAIN HEALTH</h3>
    <div class="action-grid">
      <div class="action"><span class="ico"><svg width="10" height="10" viewBox="0 0 10 10"><circle cx="5" cy="3" r="2" fill="#fff"/><path d="M1 10a4 4 0 018 0z" fill="#fff"/></svg></span><div><b>EDUCATE AND EMPOWER COMMUNITIES</b><span>Share brain health messages at gatherings and clinics.</span></div></div>
      <div class="action"><span class="ico alt"><svg width="10" height="10" viewBox="0 0 10 10"><rect x="1" y="5" width="2" height="4" fill="#fff"/><rect x="4" y="3" width="2" height="6" fill="#fff"/><rect x="7" y="1" width="2" height="8" fill="#fff"/></svg></span><div><b>COLLECT AND USE DATA</b><span>Track needs to guide planning and funding.</span></div></div>
      <div class="action"><span class="ico alt"><svg width="10" height="10" viewBox="0 0 10 10"><circle cx="3" cy="5" r="2.2" fill="none" stroke="#fff"/><circle cx="7" cy="5" r="2.2" fill="none" stroke="#fff"/></svg></span><div><b>MOBILIZE PARTNERSHIPS</b><span>Link tribal, state and local service providers.</span></div></div>
      <div class="action"><span class="ico"><svg width="10" height="10" viewBox="0 0 10 10"><path d="M5 1l4 2v3c0 2-2 3-4 4-2-1-4-2-4-4V3z" fill="#fff"/></svg></span><div><b>STRENGTHEN POLICIES</b><span>Adopt codes that protect elders with memory loss.</span></div></div>
      <div class="action"><span class="ico"><svg width="10" height="10" viewBox="0 0 10 10"><path d="M2 5l2 2 4-4" stroke="#fff" stroke-width="1.5" fill="none"/></svg></span><div><b>BUILD THE WORKFORCE</b><span>Train staff to detect and respond to dementia.</span></div></div>
      <div class="action"><span class="ico alt"><svg width="10" height="10" viewBox="0 0 10 10"><path d="M5 9L1.5 5.5A2 2 0 015 2.6 2 2 0 018.5 5.5z" fill="#fff"/></svg></span><div><b>SUPPORT CAREGIVERS</b><span>Offer respite, training and cultural support.</span></div></div>
    </div>
  </div>
  <div class="photo-row" style="margin-top:12px">
    <div class="photo photo-c" style="height:120px" role="img" aria-label="Photograph of an elder with a family member"></div>
    <div class="photo photo-b" style="height:120px" role="img" aria-label="Photograph of a health worker talking with an elder"></div>
  </div>
  <div class="page-footer"><div class="brand"><span class="brand-dot"></span>QR7</div><span class="page-num">06</span></div>
</section>

<!-- Sovereignty -->
<section class="page p-sovereignty">
  <div class="photo photo-a" style="height:150px" role="img" aria-label="Photograph of an elder couple exchanging a high five with a caregiver"></div>
  <div class="band band-rust" style="margin:-14px 0 10px 60px;position:relative">TRIBAL SOVEREIGNTY</div>
  <p class="body">Tribal sovereignty is the foundation for every policy choice described in this report. As governments, tribes may enact laws, operate courts and deliver health services that reflect their own values and responsibilities toward elders.</p>
  <p class="body">Many tribes have long traditions of caring for elders within extended families. Written codes can honor these practices while adding clear procedures for situations involving neglect, financial exploitation or loss of capacity.</p>
  <p class="body">Where jurisdiction overlaps with states, careful agreements help avoid gaps in protection. Tribes may choose to partner, contract or build their own programs depending on resources and community priorities.</p>
  <p class="body">Public health agencies serving tribal communities should respect this authority, consult early and support tribally led solutions for brain health and dementia care.</p>
  <div class="page-footer"><div class="brand"><span class="brand-dot"></span>QR7</div><span class="page-num">07</span></div>
</section>

</body>
</html>
```